Energy trading company (Voltarix) needs a business card

We need a business card for a company based in Central America. Our main purpose is trading energy . We already have the logo but we need some good creativity to design a high impact business card. Colors blue, orange, green can be used or we would like to see good combinatios with our logo

Target Market(s)

Energy

Industry/Entity Type

Power Generation

Contact Information for Business Card

Logo , headquarters , name, background

Font styles to use
Serif
Sans Serif

Colors

Designer to choose colors to be used in the design.

Requirements
Must have
• it must have a fresh and clean view
Nice to have
• good backgrounds that combine with the logo
Should not have
• too much words

```html
<!DOCTYPE html>
<html lang="en">
<head>
<meta charset="utf-8">
<title>Voltarix business card</title>
<link rel="stylesheet" href="https://fonts.googleapis.com/css2?family=Exo+2:wght@400;500&family=Roboto:wght@400;700&display=swap">
<style>
  :root {
    --backdrop: #3a3a3a;
    --card-black: #1e1e1f;
    --emboss-grey: #4a4a4c;
    --orange: #ef8c1c;
    --orange-deep: #e5801a;
    --green: #5cb83a;
    --blue: #1b7fc0;
    --white: #ffffff;
  }
  * { margin: 0; padding: 0; box-sizing: border-box; }
  html, body { width: 799px; height: 1200px; overflow: hidden; }
  body {
    background: var(--backdrop);
    position: relative;
    font-family: "Roboto", Arial, sans-serif;
  }
  .card {
    position: absolute;
    left: 80px;
    width: 640px;
    height: 366px;
    background: var(--card-black);
    box-shadow: 0 10px 30px rgba(0,0,0,.45);
    overflow: hidden;
  }
  .card--front { top: 150px; }
  .card--back { top: 660px; }

  .front-brand {
    position: absolute;
    left: 0; right: 0; top: 120px;
    text-align: center;
    font-family: "Exo 2", Arial, sans-serif;
    font-weight: 400;
    font-size: 64px;
    letter-spacing: 2px;
    color: var(--emboss-grey);
  }
  .front-web {
    position: absolute;
    left: 0; right: 0; top: 262px;
    display: flex;
    justify-content: center;
    align-items: center;
    gap: 22px;
    color: var(--white);
    font-size: 15px;
    letter-spacing: .5px;
  }
  .front-web .dash { width: 38px; height: 3px; background: var(--orange); }

  .back-art { position: absolute; inset: 0; }
  .back-brand {
    position: absolute;
    left: 44px; top: 150px;
    display: flex; align-items: center; gap: 12px;
    font-family: "Exo 2", Arial, sans-serif;
    font-weight: 500;
    font-size: 44px;
    color: var(--orange);
  }
  .back-brand .mark-dot { width: 18px; height: 18px; border-radius: 50%; background: var(--orange); }

  .contact {
    position: absolute;
    left: 400px; top: 74px;
    color: var(--white);
  }
  .contact .person { font-size: 22px; font-weight: 700; }
  .contact .role { font-size: 15px; margin-top: 2px; }
  .contact ul { list-style: none; margin-top: 22px; }
  .contact li {
    display: flex; align-items: center; gap: 10px;
    font-size: 15px; line-height: 25px;
  }
  .contact li svg { width: 14px; height: 14px; fill: var(--white); flex: none; }
  .contact .address { font-size: 15px; line-height: 21px; margin-top: 6px; }
</style>
</head>
<body>
  <section class="card card--front">
    <div class="front-brand">VOLTARIX</div>
    <div class="front-web"><span class="dash"></span><span>www.voltarix.com</span><span class="dash"></span></div>
  </section>

  <section class="card card--back">
    <svg class="back-art" viewBox="0 0 640 366" width="640" height="366">
      <defs>
        <linearGradient id="edge" x1="0" y1="0" x2="0" y2="1">
          <stop offset="0" stop-color="var(--orange)"/>
          <stop offset=".45" stop-color="var(--green)"/>
          <stop offset="1" stop-color="var(--blue)"/>
        </linearGradient>
      </defs>
      <path d="M362 0 C 336 150, 270 290, 158 366 L 640 366 L 640 0 Z" fill="url(#edge)"/>
      <path d="M372 0 C 348 150, 284 292, 174 366 L 640 366 L 640 0 Z" fill="var(--orange)"/>
    </svg>

    <div class="back-brand"><span class="mark-dot"></span>VOLTARIX</div>

    <div class="contact">
      <div class="person">Marco Reyes Luna</div>
      <div class="role">Managing Director</div>
      <ul>
        <li><svg viewBox="0 0 24 24"><path d="M6.6 10.8a15 15 0 0 0 6.6 6.6l2.2-2.2c.3-.3.7-.4 1-.2 1.1.4 2.3.6 3.6.6.6 0 1 .4 1 1V20c0 .6-.4 1-1 1A17 17 0 0 1 3 4c0-.6.4-1 1-1h3.5c.6 0 1 .4 1 1 0 1.3.2 2.5.6 3.6.1.3 0 .7-.2 1z"/></svg>555-014-2290</li>
        <li><svg viewBox="0 0 24 24"><path d="M2 5h20v14H2z M4 7v.5l8 5 8-5V7l-8 5z" fill-rule="evenodd"/></svg>marco@voltarix.com</li>
        <li><svg viewBox="0 0 24 24"><path d="M12 2a10 10 0 1 0 0 20 10 10 0 0 0 0-20zm6.9 6h-3a15 15 0 0 0-1.3-3.9A8 8 0 0 1 18.9 8zM12 4c.8 1.2 1.5 2.5 1.9 4h-3.8c.4-1.5 1.1-2.8 1.9-4zM4.3 14a8 8 0 0 1 0-4h3.4a16 16 0 0 0 0 4zm.8 2h3a15 15 0 0 0 1.3 3.9A8 8 0 0 1 5.1 16zm3-8h-3a8 8 0 0 1 4.3-3.9A15 15 0 0 0 8.1 8zM12 20c-.8-1.2-1.5-2.5-1.9-4h3.8c-.4 1.5-1.1 2.8-1.9 4zm2.3-6H9.7a14 14 0 0 1 0-4h4.6a14 14 0 0 1 0 4zm.3 5.9a15 15 0 0 0 1.3-3.9h3a8 8 0 0 1-4.3 3.9zm1.7-5.9a16 16 0 0 0 0-4h3.4a8 8 0 0 1 0 4z"/></svg>www.voltarix.com</li>
      </ul>
      <p class="address">18 Calle Solar, Barrio Norte,<br>San Mateo, CA 10450</p>
    </div>
  </section>
</body>
</html>
```